Performance and Functional Training for Life
Project: Business Card & Letterhead
Business Card & Letterhead
Bright & Fun-filled
Dale Varnek
Strength & Conditioning Coach
42 Millbrook Lane Larkmoor, NH 03499
dale@strideformlab.com
www.strideformlab.com
Whether competing on the field of play or in the game of life Stride Form Lab is your proven partner for: Performance Enhancement Injury Reduction & Rehabilitation Weight Management & Nutritional Strategies General Fitness Consulting to Companies and Schools Team Training

```html
<!DOCTYPE html>
<html lang="en">
<head>
<meta charset="utf-8">
<title>Stride Form Lab – Business Card</title>
<link href="https://fonts.googleapis.com/css2?family=Open+Sans:ital,wght@0,400;0,600;0,700;1,400;1,600;1,700&display=swap" rel="stylesheet">
<style>
  :root {
    --stage: #e4e5e7;
    --card: #ffffff;
    --blue: #1d4fb0;
    --blue-dark: #123a8c;
    --blue-light: #2f6fd6;
    --sky: #b9cdea;
    --ink: #1b1b1f;
    --grey: #8a8d93;
  }
  * { margin: 0; padding: 0; box-sizing: border-box; }
  html, body { width: 1200px; height: 895px; overflow: hidden; }
  body {
    background: var(--stage);
    font-family: "Open Sans", Arial, sans-serif;
    position: relative;
  }
  .card {
    position: absolute;
    left: 250px;
    width: 700px;
    height: 400px;
    background: var(--card);
    overflow: hidden;
    box-shadow: 0 6px 18px rgba(0,0,0,.18);
  }
  .card--front { top: 25px; }
  .card--back { top: 470px; }

  .front-shapes { position: absolute; inset: 0; }

  .holder { position: absolute; left: 40px; top: 44px; color: #fff; }
  .holder__name { font-size: 26px; font-weight: 700; }
  .holder__role { font-size: 16px; font-style: italic; opacity: .9; margin-top: 2px; }

  .contact { position: absolute; left: 40px; top: 212px; list-style: none; color: #fff; font-size: 14px; }
  .contact li { display: flex; align-items: center; gap: 10px; margin-bottom: 9px; line-height: 1.25; }
  .contact svg { flex: none; }

  .brand { position: absolute; left: 372px; top: 222px; display: flex; align-items: center; gap: 12px; }
  .brand__dot { width: 34px; height: 34px; border-radius: 50%; background: var(--blue); }
  .brand__name { font-size: 34px; font-weight: 600; color: var(--blue); letter-spacing: -.5px; }
  .brand__tagline { position: absolute; left: 372px; top: 276px; font-size: 15px; font-style: italic; font-weight: 600; color: var(--blue); }

  .watermark { position: absolute; left: 40px; top: 40px; }
  .watermark__dot { display: block; width: 150px; height: 150px; border-radius: 50%; background: var(--sky); opacity: .55; }

  .pitch { position: absolute; left: 300px; top: 78px; width: 370px; color: var(--ink); }
  .pitch__intro { font-size: 14px; font-weight: 700; font-style: italic; line-height: 1.35; margin-bottom: 8px; }
  .pitch__list { list-style: none; font-size: 14px; line-height: 1.55; }
  .pitch__list li { display: flex; align-items: center; gap: 8px; }
  .pitch__list li::before { content: ""; width: 8px; height: 8px; background: var(--blue); flex: none; }
</style>
</head>
<body>

<section class="card card--front">
  <svg class="front-shapes" width="700" height="400" viewBox="0 0 700 400" aria-hidden="true">
    <defs>
      <linearGradient id="panelBlue" x1="0" y1="0" x2="1" y2="1">
        <stop offset="0" stop-color="#2f6fd6"/>
        <stop offset="1" stop-color="#123a8c"/>
      </linearGradient>
    </defs>
    <path d="M0 0 H392 C330 120 290 270 300 400 H0 Z" fill="#2b2d33"/>
    <path d="M0 0 H372 C312 120 272 270 282 400 H0 Z" fill="#c9ccd2"/>
    <path d="M0 0 H364 C304 120 264 270 274 400 H0 Z" fill="url(#panelBlue)"/>
  </svg>

  <div class="holder">
    <p class="holder__name">Dale Varnek</p>
    <p class="holder__role">Strength &amp; Conditioning Coach</p>
  </div>

  <ul class="contact">
    <li>
      <svg width="18" height="18" viewBox="0 0 18 18"><circle cx="9" cy="9" r="9" fill="#fff"/><path d="M9 4a3 3 0 0 0-3 3c0 2.3 3 6 3 6s3-3.7 3-6a3 3 0 0 0-3-3zm0 4.2A1.2 1.2 0 1 1 9 5.8a1.2 1.2 0 0 1 0 2.4z" fill="#1d4fb0"/></svg>
      <span>42 Millbrook Lane<br>Larkmoor, NH 03499</span>
    </li>
    <li>
      <svg width="18" height="18" viewBox="0 0 18 18"><circle cx="9" cy="9" r="9" fill="#fff"/><path d="M6.2 4.5l1.6 2.2-1 1.1c.6 1.3 1.5 2.2 2.8 2.8l1.1-1 2.2 1.6-.8 1.6C9 12.6 5.4 9 5.1 5.3z" fill="#1d4fb0"/></svg>
      <span>555.204.0142</span>
    </li>
    <li>
      <svg width="18" height="18" viewBox="0 0 18 18"><circle cx="9" cy="9" r="9" fill="#fff"/><rect x="4.5" y="6" width="9" height="6.2" fill="none" stroke="#1d4fb0" stroke-width="1.2"/><path d="M4.5 6l4.5 3.5L13.5 6" fill="none" stroke="#1d4fb0" stroke-width="1.2"/></svg>
      <span>dale@strideformlab.com</span>
    </li>
    <li>
      <svg width="18" height="18" viewBox="0 0 18 18"><circle cx="9" cy="9" r="9" fill="#fff"/><circle cx="9" cy="9" r="4.5" fill="none" stroke="#1d4fb0" stroke-width="1.2"/><path d="M4.5 9h9M9 4.5c-2 2.4-2 6.6 0 9M9 4.5c2 2.4 2 6.6 0 9" fill="none" stroke="#1d4fb0" stroke-width="1"/></svg>
      <span>www.strideformlab.com</span>
    </li>
  </ul>

  <div class="brand">
    <span class="brand__dot"></span>
    <span class="brand__name">Stride Form Lab</span>
  </div>
  <p class="brand__tagline">Performance and Functional Training for Life</p>
</section>

<section class="card card--back">
  <div class="watermark" aria-hidden="true">
    <span class="watermark__dot"></span>
  </div>
  <div class="pitch">
    <p class="pitch__intro">Whether competing on the field of play or in the game of life Stride Form Lab is your proven partner for:</p>
    <ul class="pitch__list">
      <li>Performance Enhancement</li>
      <li>Injury Reduction &amp; Rehabilitation</li>
      <li>Weight Management &amp; Nutritional Strategies</li>
      <li>General Fitness</li>
      <li>Consulting to Companies and Schools</li>
      <li>Team Training</li>
    </ul>
  </div>
</section>

</body>
</html>
```